KVR Biz Cards

We are a property management company that manages luxury level residential estates. As such, we need a business card design that gives a high end feel. The idea at the moment is to list the services offered on the back of the card, and our company information on the front of the card.

Services for the back of the card are as follows:
Professional Property Management service, Home Hosting & Concierge Service, Holliday Home / Income Property Management

```html
<!DOCTYPE html>
<html lang="en">
<head>
<meta charset="utf-8">
<title>KVR Business Cards</title>
<link rel="stylesheet" href="https://fonts.googleapis.com/css2?family=Montserrat:wght@500;600;700&family=Arimo:wght@400;700&display=swap">
<style>
  :root {
    --page: #e6e8e7;
    --ink: #0d0c0b;
    --bronze: #7d4d0c;
    --bronze-bright: #8f5a15;
    --white: #ffffff;
    --card-w: 940px;
    --card-h: 537px;
  }
  * { margin: 0; padding: 0; box-sizing: border-box; }
  html, body { width: 1200px; height: 1163px; overflow: hidden; background: var(--page); }
  .canvas { position: relative; width: 1200px; height: 1163px; }
  .card {
    position: absolute; left: 130px; width: var(--card-w); height: var(--card-h);
    overflow: hidden; box-shadow: 0 14px 30px rgba(0,0,0,.28);
  }
  .card--front { top: 29px; background: var(--ink); }
  .card--back { top: 597px; background: var(--bronze); }
  .card__space {
    position: absolute; left: 0; top: 0; width: 700px; height: 400px;
    transform: scale(1.3429); transform-origin: 0 0;
  }
  .card__lines { position: absolute; inset: 0; width: 700px; height: 400px; }

  .brand { position: absolute; text-align: center; color: var(--white); font-family: "Montserrat", sans-serif; }
  .brand__mark { font-weight: 600; line-height: 1; letter-spacing: 1px; }
  .brand__name { font-weight: 600; letter-spacing: .4px; line-height: 1.1; }
  .brand__tagline { font-weight: 500; line-height: 1.1; letter-spacing: .3px; }

  .card--front .brand { left: 522px; top: 60px; width: 160px; }
  .card--front .brand__mark { font-size: 22px; margin-bottom: 5px; }
  .card--front .brand__name { font-size: 9.5px; }
  .card--front .brand__tagline { font-size: 6px; }

  .person { position: absolute; left: 60px; top: 208px; font-family: "Arimo", sans-serif; }
  .person__name { font-size: 40px; line-height: 1; color: var(--bronze-bright); letter-spacing: -.5px; }
  .person__first { font-weight: 400; }
  .person__last { font-weight: 700; }
  .person__role { margin-top: 4px; font-size: 16.5px; color: var(--white); letter-spacing: -.3px; }

  .divider { position: absolute; left: 359px; top: 174px; width: 1.5px; height: 153px; background: var(--bronze-bright); }

  .contacts { position: absolute; left: 428px; top: 172px; list-style: none; font-family: "Arimo", sans-serif; color: var(--white); font-size: 15.5px; line-height: 1.15; }
  .contacts li { display: flex; align-items: flex-start; margin-bottom: 10px; }
  .contacts svg { width: 23px; height: 23px; flex: none; margin-right: 14px; margin-top: -2px; }

  .card--back .brand { left: 180px; top: 118px; width: 340px; }
  .card--back .brand__mark { font-size: 48px; margin-bottom: 14px; }
  .card--back .brand__name { font-size: 19px; }
  .card--back .brand__tagline { font-size: 12.5px; }
  .rule { position: absolute; left: 198px; top: 239px; width: 304px; height: 1.5px; background: var(--white); }
  .services { position: absolute; left: 100px; top: 274px; width: 500px; text-align: center; color: var(--white); font-family: "Arimo", sans-serif; }
  .services__title { font-size: 16px; font-weight: 700; margin-bottom: 8px; letter-spacing: -.2px; }
  .services__list { list-style: none; font-size: 15.5px; line-height: 20px; letter-spacing: -.3px; }
  .services__list li::before { content: "\2022"; margin-right: 3px; }
</style>
</head>
<body>
<main class="canvas">

  <section class="card card--front" aria-label="Card front">
    <div class="card__space">
      <svg class="card__lines" viewBox="0 0 700 400" aria-hidden="true">
        <g fill="none" stroke="#8f5a15" stroke-width="19" stroke-linejoin="miter">
          <polyline points="137,-8 392,94 367,145"/>
          <polyline points="58,-8 -2,142"/>
          <polyline points="-8,298 157,368"/>
        </g>
      </svg>

      <div class="brand">
        <div class="brand__mark">KVR</div>
        <div class="brand__name">KINGSVALE RESIDENCES</div>
        <div class="brand__tagline">Luxury Living, Expertly Managed Daily</div>
      </div>

      <div class="person">
        <div class="person__name"><span class="person__first">DANIEL</span> <span class="person__last">REYES</span></div>
        <div class="person__role">MARKETING MANAGER</div>
      </div>

      <div class="divider"></div>

      <ul class="contacts">
        <li>
          <svg viewBox="0 0 24 24" aria-hidden="true"><circle cx="12" cy="12" r="11" fill="#8f5a15"/><rect x="6.5" y="8" width="11" height="8" fill="none" stroke="#0d0c0b" stroke-width="1.5"/><polyline points="6.5,8 12,12.5 17.5,8" fill="none" stroke="#0d0c0b" stroke-width="1.5"/></svg>
          <span>info@companyname</span>
        </li>
        <li>
          <svg viewBox="0 0 24 24" aria-hidden="true"><circle cx="12" cy="12" r="11" fill="#8f5a15"/><path d="M8 6.5l2.2 2.6-1.2 1.6c.8 1.8 2.2 3.2 4 4l1.6-1.2 2.6 2.2-1.4 2c-4.8-.6-8.6-4.4-9.2-9.2z" fill="#0d0c0b"/></svg>
          <span>+01234 567 890<br>+01234 567 890</span>
        </li>
        <li>
          <svg viewBox="0 0 24 24" aria-hidden="true"><circle cx="12" cy="12" r="11" fill="#8f5a15"/><path d="M12 6l6 5.2h-1.8V17h-3v-3.5h-2.4V17h-3v-5.8H6z" fill="#0d0c0b"/></svg>
          <span>Your city address<br>street location, state, country</span>
        </li>
        <li>
          <svg viewBox="0 0 24 24" aria-hidden="true"><circle cx="12" cy="12" r="11" fill="#8f5a15"/><circle cx="12" cy="12" r="5.5" fill="none" stroke="#0d0c0b" stroke-width="1.4"/><line x1="6.5" y1="12" x2="17.5" y2="12" stroke="#0d0c0b" stroke-width="1.2"/><ellipse cx="12" cy="12" rx="2.3" ry="5.5" fill="none" stroke="#0d0c0b" stroke-width="1.2"/></svg>
          <span>wwwyourcompanyname</span>
        </li>
      </ul>
    </div>
  </section>

  <section class="card card--back" aria-label="Card back">
    <div class="card__space">
      <svg class="card__lines" viewBox="0 0 700 400" aria-hidden="true">
        <g fill="none" stroke="#0d0c0b" stroke-width="11" stroke-linejoin="miter">
          <polyline points="6,-4 146,126 -4,282"/>
          <polyline points="704,292 592,404"/>
        </g>
      </svg>

      <div class="brand">
        <div class="brand__mark">KVR</div>
        <div class="brand__name">KINGSVALE RESIDENCES</div>
        <div class="brand__tagline">Luxury Living, Expertly Managed Daily</div>
      </div>

      <div class="rule"></div>

      <div class="services">
        <h2 class="services__title">OUR SERVICES</h2>
        <ul class="services__list">
          <li>Professional Property Management service</li>
          <li>Home Hosting &amp; Concierge Service</li>
          <li>Holliday Home / Income Property Management</li>
        </ul>
      </div>
    </div>
  </section>

</main>
</body>
</html>
```